Online-Marketing Material für Beraternetzwerk
Zielgruppe
Ich habe ein Beraternetzwerk im deutschen Gesundheitswesen gegründet, gleichzeitig einen gemeinnützigen Verein, habe zwei webseiten www.kv-pflegeberatung-demo.de + www.kv-pflegefreunde-demo.de, Logo, Briefpapier etc. sind vorhanden. Hauptfarbe GmbH RGB 185/87/120 Hex#B95778, Verein RGB 226/125/119 Hex#E27D77. Die Organisationen sind grundsätzlich getrennt, aber es gibt eine Zusammenarbeit und Partner meines Netzwerkes sind auch Fördermitglieder im Verein
Aufgabenstellung
Die beiden Firmenfarben müssen verwendet werden, für die GmbH hauptsächlich die eigene, die 2. Farbe darf mit verwendet werden. Es darf insgesamt feminin wirken, aber nicht verspielt oder gar niedlich. Ich bin Business-Frau;-). Als Schrift habe ich mich auf Avenir next konzentriert, die Agentur hat auch Alternate Gothic auf den Webseiten verwendet. Jetzt benötige ich für eine Veranstaltungsreihe die Ausarbeitung von LinkedIn, Facebook/Insta, Einladung per Brevo und E-Mail Grafiken. Es sind immer Veranstaltungen, zu denen ich einlade und in denen meine Geschäftspartner ihre Expertise gegenüber Kunden darstellen. Die Veranstaltungen sind als Duo zu sehen 1. Präsenz in München, 2. als Online Meeting ein paar Tage später. Die Location wird das Hotel Marwin, direkt am Brunnenhofplatz in München sein. Start der Präsenzveranstaltung 11:00, anschließend Mittagessen. Als Titel für die Veranstaltungen sehe ich 'KlinikForum' vor, es wird jeweils noch ein inhaltliches Thema wie z.B. 'Unternehmenskauf/-verkauf' ergänzt. Erster Termin ist vss. am 15. September 2023. Anbei auch ein paar erste Entwürfe 'meiner' Agentur nebst Feedback von mir. Ich glaube inzwischen nicht, dass hier etwas vernünftiges produziert wird, deshalb mein Versuch auf diesem Weg. Weitere Zusammenarbeit dann herzlich gerne

```html
<!DOCTYPE html>
<html lang="de">
<head>
<meta charset="utf-8">
<title>KlinikForum – Unternehmenskauf/-verkauf</title>
<link rel="stylesheet" href="https://fonts.googleapis.com/css2?family=Nunito+Sans:wght@300;600;700;800;900&display=swap">
<style>
  :root {
    --brand: #b95778;
    --brand-deep: #9a3d63;
    --brand-soft: #e09ab5;
    --partner: #e27d77;
    --white: #ffffff;
    --ink: #1a1a1a;
    --wall: #e6ddd0;
    --wall-light: #f1ebe2;
  }
  html, body {
    margin: 0;
    padding: 0;
    width: 1200px;
    height: 630px;
    overflow: hidden;
    background: var(--white);
  }
  .event-banner {
    position: relative;
    width: 1200px;
    height: 630px;
    overflow: hidden;
    font-family: "Nunito Sans", "Avenir Next", sans-serif;
    background: linear-gradient(170deg, var(--brand-soft) 0%, #f2cbd9 30%, #fbeef3 55%, var(--white) 75%);
  }
  .portrait {
    position: absolute;
    top: 0;
    right: 0;
    width: 640px;
    height: 630px;
    background:
      radial-gradient(ellipse 180px 300px at 430px 400px, #5a5e66 0%, #6b6f77 60%, rgba(107,111,119,0) 100%),
      linear-gradient(180deg, var(--wall-light) 0%, var(--wall) 100%);
    -webkit-mask-image: linear-gradient(90deg, transparent 0%, #000 40%);
            mask-image: linear-gradient(90deg, transparent 0%, #000 40%);
  }
  .event-title {
    position: absolute;
    left: 38px;
    top: 22px;
    margin: 0;
    font-size: 118px;
    line-height: 1;
    letter-spacing: 1px;
    color: var(--brand);
    white-space: nowrap;
  }
  .event-title .light { font-weight: 300; }
  .event-title .bold { font-weight: 900; }
  .event-topic {
    position: absolute;
    left: 120px;
    top: 140px;
    margin: 0;
    font-size: 40px;
    font-weight: 800;
    color: var(--brand-deep);
  }
  .date-block {
    position: absolute;
    left: 40px;
    top: 255px;
    width: 232px;
    height: 345px;
  }
  .date-block svg { position: absolute; inset: 0; }
  .date-block .date-text {
    position: absolute;
    inset: 0;
    color: var(--white);
    text-align: center;
  }
  .date-day {
    position: absolute;
    left: 0; right: 0;
    top: 52px;
    font-size: 104px;
    font-weight: 800;
    line-height: 1;
  }
  .date-month {
    position: absolute;
    left: 0; right: 0;
    top: 166px;
    font-size: 40px;
    font-weight: 600;
    line-height: 1;
  }
  .date-year {
    position: absolute;
    left: 0; right: 0;
    top: 206px;
    font-size: 76px;
    font-weight: 800;
    line-height: 1;
  }
  .venue {
    position: absolute;
    left: 300px;
    width: 416px;
    text-align: center;
    color: var(--brand);
  }
  .venue-name { top: 254px; font-size: 22px; font-weight: 800; }
  .venue-note { top: 288px; font-size: 15px; font-weight: 600; }
  .venue-format { top: 318px; font-size: 36px; font-weight: 800; }
  .venue-time { top: 358px; font-size: 74px; font-weight: 900; line-height: 1; }
  .online-band {
    position: absolute;
    left: 318px;
    top: 439px;
    width: 384px;
    height: 37px;
  }
  .online-band svg { position: absolute; inset: 0; }
  .online-band span {
    position: absolute;
    inset: 0;
    display: flex;
    align-items: center;
    justify-content: center;
    color: var(--white);
    font-size: 16px;
    font-weight: 600;
  }
  .company {
    position: absolute;
    left: 304px;
    top: 506px;
    display: flex;
    align-items: center;
    gap: 20px;
  }
  .company-dot {
    width: 84px;
    height: 84px;
    border-radius: 50%;
    background: var(--brand);
  }
  .company-name {
    font-size: 30px;
    font-weight: 800;
    line-height: 1.1;
    color: var(--ink);
  }
</style>
</head>
<body>
  <main class="event-banner">
    <div class="portrait" role="img" aria-label="Porträtfoto der Gastgeberin im dunklen Blazer mit verschränkten Armen vor einer hellen Steinwand"></div>

    <h1 class="event-title"><span class="light">KLINIK</span> <span class="bold">FORUM</span></h1>
    <p class="event-topic">“Unternehmenskauf/-verkauf”</p>

    <div class="date-block">
      <svg width="232" height="345" viewBox="0 0 232 345" aria-hidden="true">
        <polygon points="0,0 232,44 232,345 0,300" fill="var(--brand)"/>
      </svg>
      <div class="date-text">
        <div class="date-day">15.</div>
        <div class="date-month">September</div>
        <div class="date-year">2023</div>
      </div>
    </div>

    <div class="venue venue-name">im Hotel Marwin</div>
    <div class="venue venue-note">direkt am Brunnenhofplatz</div>
    <div class="venue venue-format">Präsenzveranstaltung</div>
    <div class="venue venue-time">11:00</div>

    <div class="online-band">
      <svg width="384" height="37" viewBox="0 0 384 37" aria-hidden="true">
        <polygon points="14,0 384,0 370,37 0,37" fill="var(--brand-deep)"/>
      </svg>
      <span>Online am x.xx. Die n 17:00</span>
    </div>

    <div class="company">
      <div class="company-dot"></div>
      <div class="company-name">KV Pflegeberatung<br>GmbH</div>
    </div>
  </main>
</body>
</html>
```